Our architectural studio needs a new business card

We need a business card design for our studio based in Waterloo in Belgium. We are active in architecture, design and installation.
Our works are contemporary and minimalist. our clients are refined and cultured.
Our business card must be minimalist and refined.

Project Deadline Extended
Reason: Some designers have accepted my invitation but they don't have all replied. I want to give them a chance to make one proposal. Paul

Target Market(s)

architecture

Industry/Entity Type

Business

Contact Information for Business Card

studio: paul dornevaux studio
paul dornevaux, architecte
M. +32 471 586 927
F. +322 619 4850
www.pauldornevaux-example.com
paul@pauldornevaux-example.com
14 rue des Marronniers
1420 Waterloo
Belgium

Font styles to use
Sans Serif

Requirements
Must have
• simple, minimalist, clear, elegant and chic! Black and white
Nice to have
• embossed logo, other format like a square for example
Should not have
• color, fantasy, curves, ...

```html
<!DOCTYPE html>
<html lang="fr">
<head>
<meta charset="utf-8">
<title>Paul Dornevaux Studio — Carte de visite</title>
<link rel="stylesheet" href="https://fonts.googleapis.com/css2?family=Michroma&family=Montserrat:wght@500;600;700&family=Arimo:wght@400&display=swap">
<style>
  :root {
    --backdrop: #d6d6d6;
    --card-dark: #101010;
    --card-dark-edge: #1c1c1c;
    --card-light: #ffffff;
    --ink-light: #e6e6e6;
    --ink-muted: #bdbdbd;
    --rule: #a8a8a8;
    --ink-dark: #111111;
  }
  * { box-sizing: border-box; margin: 0; padding: 0; }
  html, body {
    width: 1200px; height: 610px; overflow: hidden;
    background: var(--backdrop);
  }
  .canvas { position: relative; width: 1200px; height: 610px; }

  .card {
    position: absolute; top: 128px;
    width: 550px; height: 382px;
    border-radius: 20px; overflow: hidden;
    box-shadow: 0 3px 8px rgba(0,0,0,.25);
  }
  .card--front {
    left: 50px;
    background: radial-gradient(ellipse at 55% 45%, var(--card-dark-edge), var(--card-dark) 75%);
  }
  .card--back { left: 615px; background: var(--card-light); }

  .corner-lines { position: absolute; inset: 0; }

  .brand-mark {
    position: absolute; display: flex; align-items: center; gap: 8px;
    font-family: "Montserrat", sans-serif; font-weight: 600;
  }
  .brand-mark__square { display: block; }
  .card--front .brand-mark {
    left: 92px; top: 150px; font-size: 40px; color: var(--ink-muted); letter-spacing: 2px;
  }
  .card--front .brand-mark__square { width: 12px; height: 12px; background: var(--ink-muted); }
  .card--back .brand-mark {
    left: 0; right: 0; top: 120px; justify-content: center;
    font-size: 78px; color: var(--ink-dark); letter-spacing: 4px;
  }
  .card--back .brand-mark__square { width: 18px; height: 18px; background: var(--ink-dark); }

  .studio-name {
    position: absolute;
    font-family: "Montserrat", sans-serif; font-weight: 600;
    text-transform: uppercase; white-space: nowrap;
  }
  .card--front .studio-name {
    left: 38px; top: 248px; font-size: 11.5px; letter-spacing: 2.6px; color: var(--ink-muted);
  }
  .card--back .studio-name {
    left: 0; right: 0; text-align: center; top: 290px;
    font-size: 17px; font-weight: 700; letter-spacing: 3.4px; color: var(--ink-dark);
  }

  .divider {
    position: absolute; left: 282px; top: 102px;
    width: 2px; height: 176px; background: var(--rule);
  }

  .person { position: absolute; left: 318px; top: 110px; width: 235px; }
  .person__name {
    font-family: "Michroma", sans-serif; font-size: 15px; letter-spacing: 1.8px;
    color: var(--ink-light); text-transform: uppercase; white-space: nowrap;
  }
  .person__role {
    font-family: "Michroma", sans-serif; font-size: 11.5px; letter-spacing: 1.4px;
    color: var(--ink-muted); text-align: right; padding-right: 10px; margin-top: 2px;
  }

  .contact-list {
    position: absolute; left: 318px; top: 156px; list-style: none;
    font-family: "Arimo", sans-serif; font-size: 12.5px; color: var(--ink-light);
  }
  .contact-list li { display: flex; align-items: flex-start; height: 24.5px; }
  .contact-list .icon { width: 14px; height: 14px; margin-right: 12px; flex: none; }
  .contact-list .address { line-height: 24.5px; margin-top: -5px; }
</style>
</head>
<body>
<main class="canvas">

  <section class="card card--front" aria-label="Recto de la carte">
    <svg class="corner-lines" width="550" height="382" viewBox="0 0 550 382" aria-hidden="true">
      <polygon points="0,0 205,0 0,95" fill="#0a0a0a"/>
      <polygon points="0,240 0,382 245,382" fill="#0a0a0a"/>
      <line x1="0" y1="95" x2="205" y2="0" stroke="#9a9a9a" stroke-width="2"/>
      <line x1="0" y1="240" x2="245" y2="382" stroke="#9a9a9a" stroke-width="2"/>
    </svg>

    <div class="brand-mark"><span>PDS</span><span class="brand-mark__square"></span></div>
    <p class="studio-name">paul dornevaux studio</p>

    <div class="divider"></div>

    <div class="person">
      <p class="person__name">Paul Dornevaux</p>
      <p class="person__role">Architecte</p>
    </div>

    <ul class="contact-list">
      <li>
        <svg class="icon" viewBox="0 0 14 14" aria-hidden="true"><rect x="4" y="1" width="6" height="12" rx="1" fill="none" stroke="#ccc" stroke-width="1.2"/><circle cx="7" cy="11" r=".7" fill="#ccc"/></svg>
        <span>+32 471 586 927</span>
      </li>
      <li>
        <svg class="icon" viewBox="0 0 14 14" aria-hidden="true"><rect x="2" y="5" width="10" height="7" rx="1" fill="#ccc"/><path d="M1 5 Q7 0 13 5" fill="none" stroke="#ccc" stroke-width="1.6"/></svg>
        <span>+322 619 4850</span>
      </li>
      <li>
        <svg class="icon" viewBox="0 0 14 14" aria-hidden="true"><g fill="none" stroke="#ccc" stroke-width="1"><circle cx="7" cy="7" r="5.5"/><ellipse cx="7" cy="7" rx="2.3" ry="5.5"/><line x1="1.5" y1="7" x2="12.5" y2="7"/></g></svg>
        <span>www.pauldornevaux-example.com</span>
      </li>
      <li>
        <svg class="icon" viewBox="0 0 14 14" aria-hidden="true"><rect x="1" y="3" width="12" height="8" fill="#ccc"/><path d="M1 3 L7 8 L13 3" fill="none" stroke="#222" stroke-width="1"/></svg>
        <span>paul@pauldornevaux-example.com</span>
      </li>
      <li>
        <svg class="icon" viewBox="0 0 14 14" aria-hidden="true"><path d="M7 13 C4 9 3 7 3 5.5 A4 4 0 0 1 11 5.5 C11 7 10 9 7 13 Z" fill="#ccc"/><circle cx="7" cy="5.5" r="1.5" fill="#222"/></svg>
        <span class="address">14 rue des Marronniers<br>1420 Waterloo Belgium</span>
      </li>
    </ul>
  </section>

  <section class="card card--back" aria-label="Verso de la carte">
    <div class="brand-mark"><span>PDS</span><span class="brand-mark__square"></span></div>
    <p class="studio-name">paul dornevaux studio</p>
  </section>

</main>
</body>
</html>
```